About Us / Our Leadership Page & Graphic Design - Quillmore Solutions Software Development

NO CODE NEEDED!
Company: Quillmore Solutions
Owner: Me ( Dave )
Job: Design Quillmore Solution's About Us page
Style: See attached examples

Requirements
Include Quillmore Solution's mission, vision, and values combined with section covering the included highlights of my career in a simple, and informative manner.

The mission, vision, and value statements should be the most important aspect. Ideally they will in some way be represented through the page design and/or content.

The about us page should convey that I, Gordon Pribbley(the owner of Quillmore), am a good leader and that Quillmore Solution's customers are in great hands.

I have attached example content for the quillmore website and the theme/style. Your designs should be reflect the to the existing style

-------
CONTENT INFO
-------

[Mission]: We foster an environment with unlimited opportunity to provide innovative software and services with the highest level of quality and excellence.

[Vision]: Bring high quality software to the world in a more efficient, affordable, and reliable way; software that creates more job opportunities and higher income for developers across the world.

[Values]: Hard work, growth, creativity, and honesty

[ Top 3 highlights of my career ]
1) Agile software development consultant and software architect for TWF Holdings Partners Inc. a fortune 1000 company. Introduced Agile Development, Agile Project Management, and Agile Roadmapping while rebuilding, and continuously deploying end-of-life applications from the ground up.
2) Senior web application developer partnering with a team of 25 in an agile scrum environment for Carvantel Trust Systems we developed the Ledger Watch Grid, a high-priority fraud platform for the U.S.
3) Started and directed a software development department at an 8-figure student housing company and eventually grew the department from just one to lead a team of 5 software developers.

Through Quillmore we provide superior products and services with the highest level of quality and excellence. We specializes in:
-Web Application Development & Software Architecture
-Agile Software Development & Analysis
-Leadership & Problem Solving
-Documentation & Cross-functional Communication
-Software Testing & Debugging
-Motivation & Growth

```html
<!DOCTYPE html>
<html lang="en">
<head>
<meta charset="utf-8">
<title>About Us – Quillmore Solutions</title>
<link href="https://fonts.googleapis.com/css2?family=Roboto:wght@300;400;500;700&display=swap" rel="stylesheet">
<style>
:root{
  --bg:#232532;
  --card:#2a2d3b;
  --hero-a:#3a4150;
  --hero-b:#2c3240;
  --text:#ffffff;
  --muted:#c9cbd3;
  --soft:#9ea1ad;
  --purple:#8e5fd0;
  --green:#6dd86a;
}
*{margin:0;padding:0;box-sizing:border-box}
html,body{width:692px;height:1200px;overflow:hidden;background:var(--bg)}
body{font-family:'Roboto',sans-serif;color:var(--text);position:relative}
.abs{position:absolute}
.hero{left:0;top:0;width:692px;height:327px;background:linear-gradient(135deg,var(--hero-a),var(--hero-b) 60%,#252a35)}
.brand{left:48px;top:24px;display:flex;align-items:center;gap:6px;font-size:15px;font-weight:700;letter-spacing:.3px}
.brand-dot{width:10px;height:10px;border-radius:50%;background:var(--text)}
.nav{top:22px;left:0;width:692px;font-size:9.5px;color:var(--muted)}
.nav a{position:absolute;color:inherit;text-decoration:none}
.nav a.active{color:var(--text);font-weight:500}
.nav-dot{left:440px;top:38px;width:3px;height:3px;border-radius:50%;background:var(--green)}
.page-title{left:48px;top:148px;font-size:24px;font-weight:400}
.title-rule{left:48px;top:184px;width:40px;height:2px;background:var(--text)}
.card{background:var(--card);left:48px;width:190px}
.card h2{position:absolute;left:35px;font-size:15px;font-weight:400}
.card p{position:absolute;left:35px;width:130px;font-size:9.2px;line-height:12.3px;color:var(--muted);font-weight:300}
.icon{position:absolute}
.lead-our{left:264px;top:355px;font-size:22px;font-weight:400}
.lead-main{left:264px;top:381px;font-size:23px;font-weight:700}
.lead-text{left:264px;width:168px;font-size:9px;line-height:12.3px;color:var(--muted);font-weight:300}
.role{left:481px;font-size:13.5px;line-height:16px;color:var(--muted);font-weight:300}
.name{left:316px;top:730px;font-size:14px;font-weight:700;color:var(--muted)}
.title-ceo{left:411px;top:751px;font-size:9.5px;color:var(--soft)}
.spec-title{left:0;width:692px;top:815px;text-align:center;font-size:23px;font-weight:400}
.spec-title b{font-weight:700}
.spec-sub{left:0;width:692px;top:866px;text-align:center;font-size:15.5px;line-height:21px;font-weight:300}
.tile{background:var(--card);border-radius:4px}
.tile span{position:absolute;left:0;width:100%;text-align:center;font-size:8.5px;line-height:12px;color:var(--muted);text-transform:uppercase}
</style>
</head>
<body>

<div class="abs hero" role="img" aria-label="Photo of an office wall covered with coloured sticky notes on an agile board"></div>

<div class="abs brand"><span class="brand-dot"></span>Quillmore</div>
<nav class="abs nav">
  <a style="left:386px">Home</a>
  <a class="active" style="left:428px">About</a>
  <a style="left:471px">Overview</a>
  <a style="left:526px">Process</a>
  <a style="left:577px">Blog</a>
  <a style="left:613px">Contact</a>
</nav>
<div class="abs nav-dot"></div>

<h1 class="abs page-title">About Us</h1>
<div class="abs title-rule"></div>

<section class="abs card" style="top:214px;height:113px">
  <h2 style="top:15px">Mission</h2>
  <p style="top:41px">We foster an environment with unlimited opportunity to provide innovative software and services with the highest level of quality and excellence.</p>
</section>
<section class="abs card" style="top:332px;height:136px">
  <h2 style="top:18px">Vision</h2>
  <p style="top:46px">Bring high quality software to the world in a more efficient, affordable, and reliable way; software that creates more job opportunities and higher income for developers across the world.</p>
</section>
<section class="abs card" style="top:472px;height:110px">
  <h2 style="top:30px">Values</h2>
  <p style="top:57px">Hard work, growth, creativity, and honesty</p>
</section>

<svg class="icon" style="left:20px;top:242px" width="56" height="52" viewBox="0 0 56 52" fill="none">
  <circle cx="22" cy="32" r="17" stroke="var(--purple)" stroke-width="2"/>
  <circle cx="22" cy="32" r="11" stroke="var(--purple)" stroke-width="2"/>
  <circle cx="22" cy="32" r="5" stroke="var(--purple)" stroke-width="2"/>
  <path d="M22 32 L48 6" stroke="var(--green)" stroke-width="2"/>
  <path d="M44 4 L50 10 M46 2 L52 8" stroke="var(--green)" stroke-width="2"/>
</svg>
<svg class="icon" style="left:22px;top:382px" width="52" height="34" viewBox="0 0 52 34" fill="none">
  <path d="M2 17 Q26 -6 50 17 Q26 40 2 17Z" stroke="var(--purple)" stroke-width="2"/>
  <circle cx="26" cy="17" r="9" stroke="var(--purple)" stroke-width="2"/>
  <circle cx="26" cy="17" r="6" fill="var(--green)"/>
  <circle cx="26" cy="17" r="2.5" fill="var(--bg)"/>
</svg>
<svg class="icon" style="left:22px;top:500px" width="52" height="46" viewBox="0 0 52 46" fill="none">
  <path d="M26 3 L31 8 L26 13 L21 8Z M8 10 L13 15 L8 20 L3 15Z M44 10 L49 15 L44 20 L39 15Z" stroke="var(--green)" stroke-width="1.8"/>
  <path d="M16 22 H36 L42 28 L26 44 L10 28Z M10 28 H42 M20 22 L26 44 L32 22" stroke="var(--purple)" stroke-width="1.8"/>
</svg>

<h2 class="abs lead-our">OUR</h2>
<h2 class="abs lead-main">LEADERSHIP</h2>

<svg class="abs" style="left:0;top:0" width="692" height="1200" viewBox="0 0 692 1200" fill="none">
  <path d="M423 396 H436 Q454 396 454 414 V700 Q454 719 436 719 H212" stroke="var(--purple)" stroke-width="2"/>
  <circle cx="419" cy="396" r="4" stroke="var(--purple)" stroke-width="2" fill="var(--bg)"/>
  <path d="M142 587 V666" stroke="var(--purple)" stroke-width="2"/>
  <circle cx="142" cy="583" r="4" stroke="var(--purple)" stroke-width="2" fill="var(--bg)"/>
  <g stroke="var(--green)" stroke-width="2" fill="var(--bg)">
    <circle cx="454" cy="444" r="14"/>
    <circle cx="454" cy="551" r="14"/>
    <circle cx="454" cy="659" r="14"/>
  </g>
  <g stroke="var(--green)" stroke-width="1.2" fill="none">
    <circle cx="454" cy="444" r="11" fill="var(--green)"/>
    <path d="M454 437 L449 451 M454 437 L459 451 M450 447 H458" stroke="var(--bg)" stroke-width="1.5"/>
    <circle cx="454" cy="551" r="11" fill="var(--green)"/>
    <path d="M451 547 L448 551 L451 555 M457 547 L460 551 L457 555" stroke="var(--bg)" stroke-width="1.5"/>
    <circle cx="454" cy="659" r="11" fill="var(--green)"/>
    <circle cx="454" cy="658" r="3.5" stroke="var(--bg)" stroke-width="1.5"/>
    <path d="M454 651 V652 M447 658 H448 M460 658 H461 M449 653 L450 654 M459 653 L458 654 M452 664 H456" stroke="var(--bg)" stroke-width="1.5"/>
  </g>
  <circle cx="111" cy="688" r="42" fill="var(--green)"/>
  <circle cx="185" cy="757" r="25" fill="var(--text)"/>
  <circle cx="151" cy="719" r="63" fill="var(--purple)"/>
  <circle cx="149" cy="721" r="58" fill="#5a4a44" role="img" aria-label="Portrait photo of Gordon Pribbley, CEO"/>
  <circle cx="703" cy="418" r="16" fill="#4c4f5b"/>
  <path d="M688 424 A40 40 0 0 0 690 517" stroke="#5a5d69" stroke-width="2" stroke-dasharray="1 4"/>
  <circle cx="655" cy="523" r="9" stroke="#5a5d69" stroke-width="1.5"/>
  <circle cx="8" cy="610" r="8" fill="#4c4f5b"/>
  <path d="M14 614 A32 32 0 0 1 2 669" stroke="#5a5d69" stroke-width="1.5" stroke-dasharray="1 4"/>
  <circle cx="40" cy="671" r="5" stroke="#5a5d69" stroke-width="1.5"/>
  <circle cx="55" cy="801" r="12" stroke="#5a5d69" stroke-width="1.5"/>
  <circle cx="64" cy="794" r="8" fill="var(--green)"/>
  <rect x="630" y="898" width="9" height="9" fill="var(--green)"/>
  <rect x="634" y="891" width="11" height="11" stroke="var(--muted)" stroke-width="1"/>
</svg>

<p class="abs lead-text" style="top:421px">Agile software development consultant and software architect for TWF Holdings Partners Inc. a fortune 1000 company. Introduced Agile Development, Agile Project Management, and Agile Roadmapping while rebuilding, and continuously deploying end-of-life applications from the ground up.</p>
<p class="abs lead-text" style="top:539px">Senior web application developer partnering with a team of 25 in an agile scrum environment for Carvantel Trust Systems we developed the Ledger Watch Grid, a high-priority fraud platform for the U.S.</p>
<p class="abs lead-text" style="top:635px">Started and directed a software development department at an 8-figure student housing company and eventually grew the department from just one to lead a team of 5 software developers.</p>

<div class="abs role" style="top:428px">Software Architect<br>and Consultant</div>
<div class="abs role" style="top:535px">Senior Application<br>Developer</div>
<div class="abs role" style="top:642px">Director of Software<br>Development</div>

<div class="abs name">Gordon Pribbley</div>
<div class="abs title-ceo">CEO</div>

<h2 class="abs spec-title">WE <b>SPECIALIZE IN</b></h2>
<p class="abs spec-sub">Through Quillmore we provide superior products and services<br>with the highest level of quality and excellence.</p>

<div class="abs tile" style="left:48px;top:928px;width:193px;height:112px">
  <svg class="icon" style="left:79px;top:21px" width="34" height="34" viewBox="0 0 34 34" fill="none" stroke="var(--purple)" stroke-width="1.5"><rect x="2" y="2" width="30" height="30" rx="2"/><path d="M2 8 H32 M13 15 L9 19 L13 23 M21 15 L25 19 L21 23"/></svg>
  <span style="top:71px">Web Application Development &amp;<br>Software Architecture</span>
</div>
<div class="abs tile" style="left:248px;top:928px;width:196px;height:112px">
  <svg class="icon" style="left:81px;top:21px" width="34" height="34" viewBox="0 0 34 34" fill="none" stroke="var(--purple)" stroke-width="1.5"><circle cx="17" cy="18" r="9"/><path d="M6 3 L6 10 M3 6 L6 3 L9 6 M28 24 L28 31 M25 28 L28 31 L31 28"/></svg>
  <span style="top:71px">Agile Software<br>Development &amp; Analysis</span>
</div>
<div class="abs tile" style="left:451px;top:928px;width:194px;height:112px">
  <svg class="icon" style="left:80px;top:21px" width="34" height="34" viewBox="0 0 34 34" fill="none" stroke="var(--purple)" stroke-width="1.5"><path d="M11 17 A6 6 0 1 1 23 17 C23 21 20 22 20 25 H14 C14 22 11 21 11 17Z M14 28 H20 M17 4 V7 M5 17 H8 M26 17 H29 M8 8 L10 10 M26 8 L24 10"/></svg>
  <span style="top:71px">Leadership &amp;<br>Problem Solving</span>
</div>
<div class="abs tile" style="left:48px;top:1046px;width:193px;height:111px">
  <svg class="icon" style="left:79px;top:17px" width="36" height="36" viewBox="0 0 36 36" fill="none" stroke="var(--purple)" stroke-width="1.5"><circle cx="15" cy="15" r="12"/><path d="M24 24 L34 34 M13 11 L9 15 L13 19 M17 11 L21 15 L17 19"/></svg>
  <span style="top:68px">Software Testing &amp;<br>Debugging</span>
</div>
<div class="abs tile" style="left:248px;top:1046px;width:196px;height:111px">
  <svg class="icon" style="left:81px;top:17px" width="36" height="34" viewBox="0 0 36 34" fill="none" stroke="var(--purple)" stroke-width="1.5"><path d="M12 2 H34 V18 H24 L18 24 V18 H12Z M12 10 H2 V26 H8 V32 L14 26 H22 V18"/></svg>
  <span style="top:68px">Documentation &amp; Cross-Functional<br>Communication</span>
</div>
<div class="abs tile" style="left:451px;top:1046px;width:194px;height:111px">
  <svg class="icon" style="left:82px;top:19px" width="32" height="30" viewBox="0 0 32 30" fill="none" stroke="var(--purple)" stroke-width="1.5"><rect x="2" y="16" width="7" height="12"/><rect x="13" y="9" width="7" height="19"/><rect x="24" y="2" width="7" height="26"/></svg>
  <span style="top:68px">Motivation &amp;<br>Growth</span>
</div>

</body>
</html>
```